Local fast-growing company in the service sector

We are looking for a modern business card design, which should also appear on our letterheads

Target Market(s)

Private and industrial sectors

Contact Information for Business Card

Vorname Name
Kellbacher Str. 38
74819 Hollenstadt
Tel.: 07162-418395-0
Name@service-tkwl.de

Colors
9d9d9d
919191
aaaaaa

Requirements
Must have
• The logo (file) in silver

```html
<!DOCTYPE html>
<html lang="de">
<head>
<meta charset="utf-8">
<title>TKWL Visitenkarte</title>
<link rel="stylesheet" href="https://fonts.googleapis.com/css2?family=Exo+2:wght@700&family=Questrial&display=swap">
<style>
  :root {
    --stage: #e4e4e4;
    --card-dark: #2b2b2d;
    --card-dark-glow: #454547;
    --silver-light: #f0f0f0;
    --silver-mid: #d4d4d4;
    --silver: #aaaaaa;
    --silver-deep: #9d9d9d;
    --ink: #2a2a2a;
    --shadow: rgba(0,0,0,0.25);
  }
  html, body {
    margin: 0;
    width: 1200px;
    height: 576px;
    overflow: hidden;
    background: var(--stage);
  }
  .canvas { position: relative; width: 1200px; height: 576px; }
  .card {
    position: absolute;
    top: 138px;
    border-radius: 13px;
    overflow: hidden;
    box-shadow: 0 3px 8px var(--shadow);
  }
  .card--front {
    left: 82px; width: 484px; height: 294px;
    background: radial-gradient(ellipse at 50% 40%, var(--card-dark-glow) 0%, var(--card-dark) 70%);
  }
  .card--back {
    left: 602px; width: 480px; height: 292px;
    background: var(--card-dark);
  }
  .card__waves { position: absolute; inset: 0; }
  .brand {
    position: absolute;
    display: flex;
    align-items: center;
    gap: 14px;
    font-family: "Exo 2", sans-serif;
    font-weight: 700;
    color: var(--silver-mid);
    line-height: 1;
  }
  .brand__mark { background: var(--silver); }
  .card--front .brand {
    left: 0; right: 0; top: 112px;
    justify-content: center;
    font-size: 66px;
    letter-spacing: 2px;
  }
  .card--front .brand__mark { width: 52px; height: 52px; }
  .card--back .brand {
    left: 30px; top: 48px;
    font-size: 56px;
    letter-spacing: 2px;
  }
  .card--back .brand__mark { width: 44px; height: 44px; }
  .holder {
    position: absolute;
    left: 30px; top: 250px;
    margin: 0;
    font-family: "Exo 2", sans-serif;
    font-weight: 700;
    font-size: 17px;
    letter-spacing: 1.6px;
    color: var(--ink);
  }
  .contact {
    position: absolute;
    right: 20px; top: 181px;
    margin: 0;
    text-align: right;
    font-family: "Questrial", sans-serif;
    font-size: 13.5px;
    color: var(--ink);
    font-style: normal;
  }
  .contact__line { display: block; line-height: 17px; }
  .contact__gap { display: block; height: 4px; }
  .contact__icon {
    display: inline-block;
    width: 9px; height: 9px;
    margin-left: 4px;
    vertical-align: -1px;
  }
</style>
</head>
<body>
<main class="canvas">
  <section class="card card--front" aria-label="Vorderseite">
    <div class="brand"><span class="brand__mark"></span><span class="brand__name">TKWL</span></div>
  </section>

  <section class="card card--back" aria-label="Rückseite">
    <svg class="card__waves" viewBox="0 0 480 292" width="480" height="292" aria-hidden="true">
      <defs>
        <linearGradient id="silverFace" x1="0" y1="0" x2="1" y2="1">
          <stop offset="0" stop-color="#f2f2f2"/>
          <stop offset="1" stop-color="#cfcfcf"/>
        </linearGradient>
        <radialGradient id="darkFace" cx="0.3" cy="0.3" r="0.8">
          <stop offset="0" stop-color="#424244"/>
          <stop offset="1" stop-color="#262628"/>
        </radialGradient>
      </defs>
      <rect width="480" height="292" fill="url(#darkFace)"/>
      <path d="M0,168 C90,182 170,190 260,160 S410,80 480,66 L480,76 C410,94 330,150 250,178 C170,200 90,192 0,178 Z" fill="url(#silverFace)"/>
      <path d="M0,176 C90,196 160,212 250,190 S400,100 480,80 L480,292 L0,292 Z" fill="url(#silverFace)"/>
      <path d="M0,184 C70,196 140,206 210,198 C150,218 60,214 0,202 Z" fill="#303032"/>
    </svg>

    <div class="brand"><span class="brand__mark"></span><span class="brand__name">TKWL</span></div>

    <p class="holder">VORNAME NAME</p>

    <address class="contact">
      <span class="contact__line">Kellbacher Str. 38</span>
      <span class="contact__line">74819 Hollenstadt</span>
      <span class="contact__gap"></span>
      <span class="contact__line">07162-418395-0<svg class="contact__icon" viewBox="0 0 10 10"><path d="M1,3 Q5,0 9,3 L8,4.5 L6.5,3.5 L3.5,3.5 L2,4.5 Z M2.5,5 L7.5,5 L8.5,9 L1.5,9 Z" fill="#2a2a2a"/></svg></span>
      <span class="contact__line">www.service-tkwl.de<svg class="contact__icon" viewBox="0 0 10 10"><rect x="0.5" y="2" width="9" height="6.5" fill="#2a2a2a"/><path d="M0.5,2 L5,6 L9.5,2" stroke="#eee" stroke-width="0.9" fill="none"/></svg></span>
      <span class="contact__line">Name@service-tkwl.de<svg class="contact__icon" viewBox="0 0 10 10"><circle cx="5" cy="5" r="4.3" fill="#2a2a2a"/><path d="M0.7,5 H9.3 M5,0.7 V9.3 M5,0.7 Q2,5 5,9.3 M5,0.7 Q8,5 5,9.3" stroke="#eee" stroke-width="0.6" fill="none"/></svg></span>
    </address>
  </section>
</main>
</body>
</html>
```